Tulven Electrics Flyer Design Advertising

I am after an A5 Flyer design to help promote my electrical services business.
I would like to have information on what my business offers, photos of electrical work, and specials/deals for an amount of time.

Industry/Entity Type

Electrician

Font styles to use
Sans Serif

Colors
0292cd
33a6d7
85cae6
3176b5
333333
1b1b1b
ffffff
5c5c5c
474747

Requirements
Must have
• Specialising in New homes, renovations and commercial projects
• Contact details:
• ph. 0437 619 458
• email admin@tulvenelectrics.example.au
• facebook TulvenElectrics
• Specials/Deals:
• 10% off all electrical services
• or
• Free LED downlights on installation
• *Terms conditions apply
• ALL RESIDENTIAL & COMMERCIAL ELECTRICAL SERVICES
• - New Home installations
• - Commercial projects
• - Shop fit outs
• - Renovations
• - Smoke Detectors
• - Air Conditioning and Ceiling Fans
• - Garden Lighting
• - Oven and Cooktop Installations
• - Power Point installation
• - LED lighting upgrades
• - Security Lighting
• - Switchboard upgrades
• - Test and Tag
• - Commercial Property
• - General Electrical Maintenance

```html
<!DOCTYPE html>
<html lang="en">
<head>
<meta charset="utf-8">
<title>Tulven Electrics – A5 Flyer</title>
<link rel="stylesheet" href="https://fonts.googleapis.com/css2?family=Ubuntu:wght@300;400;500;700&display=swap">
<style>
  :root {
    --blue: #0292cd;
    --blue-mid: #33a6d7;
    --blue-light: #85cae6;
    --blue-deep: #3176b5;
    --charcoal: #333333;
    --ink: #1b1b1b;
    --white: #ffffff;
    --grey: #5c5c5c;
    --grey-dark: #474747;
    --stage: #d9d9d9;
    --paper-top: #f4f4f4;
    --paper-bottom: #dedede;
  }
  * { box-sizing: border-box; margin: 0; padding: 0; }
  html, body { width: 1200px; height: 616px; overflow: hidden; }
  body { background: var(--stage); font-family: "Ubuntu", Arial, sans-serif; position: relative; }

  .flyer {
    position: absolute; left: 384px; top: 0; width: 431px; height: 616px; overflow: hidden;
    background: linear-gradient(180deg, var(--paper-top) 0%, var(--paper-bottom) 100%);
  }
  .hero-art { position: absolute; left: 0; top: 0; width: 431px; height: 300px; }

  .brand { position: absolute; left: 245px; top: 12px; display: flex; align-items: center; gap: 8px; }
  .brand-dot { width: 30px; height: 30px; border-radius: 50%; background: var(--charcoal); }
  .brand-name { font-weight: 700; font-size: 17px; color: var(--charcoal); letter-spacing: 0.5px; line-height: 1; }

  .deal-badge { position: absolute; left: 246px; top: 110px; width: 164px; height: 164px; }
  .deal-badge svg { position: absolute; inset: 0; width: 100%; height: 100%; }
  .deal-text {
    position: absolute; inset: 0; display: flex; flex-direction: column; align-items: center; justify-content: center;
    color: var(--white); text-align: center; font-weight: 300; font-size: 11px; line-height: 1.08; text-transform: uppercase;
  }
  .deal-text .deal-big { font-size: 19px; font-weight: 400; line-height: 1; }
  .deal-text .deal-or { font-size: 10px; margin-top: 3px; }

  .headline {
    position: absolute; left: 16px; top: 272px; width: 410px; text-align: center;
    color: var(--blue); text-transform: uppercase; line-height: 1.05;
  }
  .headline .line-1 { font-size: 28px; font-weight: 700; }
  .headline .line-2 { font-size: 21px; font-weight: 700; }
  .headline .soft { font-weight: 300; color: var(--grey-dark); font-size: 0.72em; }

  .services { position: absolute; left: 16px; top: 336px; width: 200px; }
  .services-title { font-size: 11.2px; font-weight: 700; color: var(--grey-dark); line-height: 1.2; text-transform: uppercase; margin-bottom: 6px; }
  .services-list { list-style: none; }
  .services-list li { font-size: 9.6px; color: var(--ink); line-height: 13.6px; padding-left: 15px; position: relative; }
  .services-list li::before {
    content: ""; position: absolute; left: 4px; top: 4.5px; width: 5px; height: 5px; border-radius: 50%; background: var(--blue);
  }
  .divider { position: absolute; left: 216px; top: 340px; width: 1px; height: 225px; background: #c9c9c9; }

  .work-photo {
    position: absolute; width: 92px; height: 92px; border-radius: 50%;
    border: 2px solid var(--blue-mid); box-shadow: 0 2px 5px rgba(0,0,0,0.25);
  }
  .work-photo.living { left: 236px; top: 364px; background: linear-gradient(135deg, #e9eef0, #a9b8b6 60%, #6f8a7d); }
  .work-photo.lounge { left: 314px; top: 368px; background: linear-gradient(135deg, #f1efe9, #d8cfc4 55%, #c0412f); }
  .work-photo.kitchen { left: 236px; top: 442px; background: linear-gradient(160deg, #8d9297, #4a4f55 55%, #d9dadb); }
  .work-photo.dining { left: 318px; top: 448px; background: linear-gradient(145deg, #efe8de, #c9b59c 55%, #7b5b3d); }

  .contact-bar {
    position: absolute; left: 0; bottom: 0; width: 431px; height: 38px;
    background: linear-gradient(90deg, var(--blue) 0%, var(--blue-mid) 55%, var(--blue-deep) 100%);
    display: flex; align-items: center; padding-left: 18px; color: var(--white);
  }
  .contact-phone { font-size: 16px; font-weight: 700; letter-spacing: 0.5px; }
  .contact-sep { margin: 0 9px 0 12px; font-size: 12px; }
  .contact-email { font-size: 10.5px; }
  .contact-social { display: flex; align-items: center; gap: 5px; margin-left: 9px; font-size: 11px; }
  .social-dot { width: 13px; height: 13px; border-radius: 50%; background: var(--white); }
</style>
</head>
<body>
  <main class="flyer">
    <svg class="hero-art" viewBox="0 0 431 300" aria-hidden="false">
      <defs>
        <linearGradient id="house-tones" x1="0" y1="0" x2="1" y2="1">
          <stop offset="0" stop-color="#5f7b8d"/>
          <stop offset="0.45" stop-color="#c9c3b4"/>
          <stop offset="0.75" stop-color="#e8c16a"/>
          <stop offset="1" stop-color="#3f6a2d"/>
        </linearGradient>
      </defs>
      <path d="M0,205 Q150,250 262,150 L275,150 Q165,275 0,238 Z" fill="var(--charcoal)"/>
      <path d="M0,242 Q190,268 300,195 Q370,152 431,150 L431,160 Q372,165 302,210 Q190,280 0,256 Z" fill="var(--blue)"/>
      <path d="M0,0 H238 A205,205 0 0 1 0,212 Z" fill="url(#house-tones)" role="img" aria-label="Photo of a lit-up weatherboard family home at dusk"/>
      <path d="M238,0 A205,205 0 0 1 0,212" fill="none" stroke="var(--blue)" stroke-width="4"/>
    </svg>

    <div class="brand">
      <span class="brand-dot"></span>
      <span class="brand-name">TULVEN ELECTRICS</span>
    </div>

    <div class="deal-badge">
      <svg viewBox="0 0 100 100" aria-hidden="true">
        <polygon fill="var(--charcoal)" stroke="#e6e6e6" stroke-width="1" points="100,50 94.5,57 97.6,65.5 90.1,70.4 90.5,79.4 81.8,81.8 79.4,90.5 70.4,90.1 65.5,97.6 57,94.5 50,100 43,94.5 34.5,97.6 29.6,90.1 20.6,90.5 18.2,81.8 9.5,79.4 9.9,70.4 2.4,65.5 5.5,57 0,50 5.5,43 2.4,34.5 9.9,29.6 9.5,20.6 18.2,18.2 20.6,9.5 29.6,9.9 34.5,2.4 43,5.5 50,0 57,5.5 65.5,2.4 70.4,9.9 79.4,9.5 81.8,18.2 90.5,20.6 90.1,29.6 97.6,34.5 94.5,43"/>
      </svg>
      <div class="deal-text">
        <span>Specials/Deals:</span>
        <span class="deal-big">10% Off</span>
        <span>All Electrical</span>
        <span>Services</span>
        <span class="deal-or">Or</span>
        <span class="deal-big">Free</span>
        <span>LED Downlights</span>
        <span>On Installation</span>
      </div>
    </div>

    <h1 class="headline">
      <span class="line-1">Specialising <span class="soft">in</span> New Homes,</span><br>
      <span class="line-2">Renovations <span class="soft">and</span> Commercial <span class="soft">projects</span></span>
    </h1>

    <section class="services">
      <h2 class="services-title">All Residential &amp; Commercial<br>Electrical Services</h2>
      <ul class="services-list">
        <li>New Home installations</li>
        <li>Commercial projects</li>
        <li>Shop fit outs</li>
        <li>Renovations</li>
        <li>Smoke Detectors</li>
        <li>Air Conditioning and Ceiling Fans</li>
        <li>Garden Lighting</li>
        <li>Oven and Cooktop Installations</li>
        <li>Power Point installation</li>
        <li>LED lighting upgrades</li>
        <li>Security Lighting</li>
        <li>Switchboard upgrades</li>
        <li>Test and Tag</li>
        <li>Commercial Property</li>
        <li>General Electrical Maintenance</li>
      </ul>
    </section>
    <div class="divider"></div>

    <div class="work-photo living" role="img" aria-label="Photo of a bright living room with pendant lighting"></div>
    <div class="work-photo lounge" role="img" aria-label="Photo of a lounge with downlights and artwork"></div>
    <div class="work-photo kitchen" role="img" aria-label="Photo of a modern kitchen with pendant lights"></div>
    <div class="work-photo dining" role="img" aria-label="Photo of a dining area with feature lighting"></div>

    <footer class="contact-bar">
      <span class="contact-phone">0437 619 458</span>
      <span class="contact-sep">|</span>
      <span class="contact-email">admin@tulvenelectrics.example.au</span>
      <span class="contact-social"><span class="social-dot"></span>TulvenElectrics</span>
    </footer>
  </main>
</body>
</html>
```